Crestline Indoor Rowing Center Website

We need a very clean, professional and appealing website for a new company based in Avon, CT (USA) called "Crestline Indoor Rowing Center." Basically, this company as implied by its name is an indoor rowing center that consists of indoor rowing machines (Norvex 7 ergometers, http://www.norvex7.example) and a rowing simulator (called a "glidetrainer", (http://www.oarworkslab.example). These ergometers and simulators will in turn be interfaced with visualization and analysis software (www.strokeviewsoft.example) to display "virtual" races and training sessions.

Ultimately, the company will also offer advanced video analysis and 1-1 coaching, but the key message here is to leverage off the company name "Crestline" (which is a term for taking 10 very hard strokes during a rowing race) and the tagline that describes the company ("Indoor Rowing Center").

We have just completed a contest to establish the company's new logo (which I am attaching to this application) and we have some other photos that we think would be helpful in visually describing the company and its services (which I will also attach).

Part of what we like about he logo we selected are the color patterns (which will contrast nicely on both light and dark backgrounds) and the way the concept of a rower is built into the name. In addition, I like the way the number 10 subtly implies IO (as in "input and output" and/or binary numbers to also indicate a "technological dimension" to the company's services).

Also, one of the websites that we really like (that offers a similar progarm and service) in the New York City area is: http://www.harborlane-oars.example. The site is clean, informative and easy to navigate. In terms of pages, we'd be looking for the following:

Home
Info (with sub pages for About, Code of Conduct, Experience the Difference, and Careers)
Coaches
Programs*
Blog
Contact
Donate!

*Note that the various programs will be offered and managed through a third-party tool (www.heatlistpro.example) and (https://wiki.heatlistpro.example/display/FAQ/FAQs#FAQs-WhatfeaturesareavailablethroughyourClubManagementservice%3F) to allow clients to register, sign an electronic waiver and pay for programs and annual memberships. An example of these links is also available at another popular rowing web page, Tidewater Sculling in Boston, MA (https://www.tidewatersculling.example/signup/) or possibly another sign up service called "QuellSlot" (https://www.quellslotonline.example/?ql=softwrfooter)

Finally, we would also like to have links in the navigation bar to connect to social networking sites like Chatterloop, Workmesh, Vantrix+, etc.

Lastly, I realize that SketchHive specializes in design only, but we would be interested in receiving estimates for a "turn-key" project that would include coding (or if there are specific partners your design firm works with to codify your designs).

Please let me know if you have any questions or if I can provide any additional information.

Thank you!

Tobias

Target Market(s)

Please refer to the attached Powerpoint document for information about target market and the company's vision and mission.

Industry/Entity Type

Electronic

Requirements
Must have
• Clean, intuitive, highly visual and professional look and feel. A color patter and "style guide" that works effectively with the colors and design of our logo that we can build off of as we have new content.

```html
<!DOCTYPE html>
<html lang="en">
<head>
<meta charset="utf-8">
<title>Crestline Indoor Rowing Center</title>
<link href="https://fonts.googleapis.com/css2?family=Fredoka:wght@600&family=Roboto+Condensed:wght@400;700&family=Open+Sans:wght@400;600&display=swap" rel="stylesheet">
<style>
:root{
  --orange:#f26a10;
  --orange-dark:#d95a05;
  --ink:#333;
  --text:#555;
  --nav:#5e4f52;
  --panel:#ffffff;
  --paper:#efefef;
  --footer:#1c1c1c;
  --footer-bottom:#111;
  --footer-text:#ddd;
}
*{margin:0;padding:0;box-sizing:border-box}
html,body{width:961px;height:1200px;overflow:hidden}
body{position:relative;font-family:"Roboto Condensed",sans-serif;color:var(--text);
  background:linear-gradient(180deg,#e9e3dc 0%,#d8cfc6 20%,#e6ddd3 45%,#f3eee9 62%,var(--paper) 70%,var(--paper) 100%)}
.abs{position:absolute}
.hero-bg{left:0;top:0;width:961px;height:700px;
  background:radial-gradient(ellipse at 20% 30%,rgba(255,235,190,.7),transparent 55%),radial-gradient(ellipse at 85% 25%,rgba(120,110,170,.35),transparent 50%),radial-gradient(ellipse at 60% 90%,rgba(240,190,110,.35),transparent 55%)}
.brand{left:88px;top:10px}
.brand-name{font-family:"Fredoka",sans-serif;font-size:50px;line-height:52px;color:var(--orange)}
.brand-tag{font-family:"Open Sans",sans-serif;font-weight:600;font-size:10.5px;letter-spacing:3.4px;color:var(--ink);margin-top:2px}
.btn-login{left:684px;top:0;width:82px;height:23px;background:var(--orange);color:#fff;font-weight:700;font-size:12px;line-height:23px;text-align:center}
.btn-register{left:770px;top:0;width:95px;height:23px;background:#fff;color:var(--ink);font-weight:700;font-size:12px;line-height:23px;text-align:center}
.search{left:668px;top:53px;width:181px;height:26px;background:#fff;font-size:11px;color:#444;line-height:26px;padding-left:43px}
.search-btn{left:849px;top:53px;width:31px;height:26px;background:var(--orange)}
.nav{left:78px;top:90px;width:806px;height:36px;background:linear-gradient(180deg,#6d5e61,#4e4245);border-right:9px solid var(--orange)}
.nav-home{left:0;top:0;width:41px;height:36px;background:var(--orange)}
.nav-item{top:0;height:36px;line-height:36px;font-size:12.5px;color:#fff}
.nav-sep{top:0;width:0;height:36px;border-left:1px dotted rgba(255,255,255,.35)}
.slider{left:76px;top:142px;width:808px;height:315px;background:#fff;box-shadow:0 1px 6px rgba(0,0,0,.15)}
.slide{left:14px;top:10px;width:783px;height:294px;background:linear-gradient(135deg,#cfcfcf,#8a8a8a 45%,#5b5b5b 70%,#b9b9b9)}
.arrow{width:32px;height:32px;border-radius:50%;background:rgba(255,255,255,.35)}
.welcome{left:63px;top:491px;width:835px;height:205px;background:rgba(255,255,255,.85)}
.welcome h1{position:absolute;left:0;top:16px;width:835px;text-align:center;font-family:"Fredoka",sans-serif;font-size:24px;color:var(--orange);font-weight:600}
.rule{border-top:1px dashed #bbb}
.welcome p{position:absolute;left:24px;width:794px;font-size:11.6px;line-height:18px;color:var(--text)}
.welcome strong{color:var(--ink)}
.btn-dark{background:#222;color:#fff;border:4px solid #ddd;text-align:center}
.col-title{top:708px;font-family:"Fredoka",sans-serif;font-size:19px;color:#555}
.col-title span{color:var(--orange)}
.vsep{top:717px;width:0;height:297px;border-left:1px solid #ddd}
.frame{background:#fff;box-shadow:0 0 3px rgba(0,0,0,.2)}
.copy{font-size:11.6px;line-height:17px;color:#333;text-align:justify}
.post-title{font-size:13px;font-weight:700;color:#555}
.post-by{font-size:9.5px;color:#333;text-align:right}
.post-by b{color:var(--orange)}
.badge{width:48px;height:48px;border-radius:50%;overflow:hidden;text-align:center;color:#fff}
.badge .top{background:var(--orange);height:29px;padding-top:3px;font-size:9.5px;line-height:10px}
.badge .top b{display:block;font-size:13px;line-height:14px}
.badge .bot{background:#222;height:19px;font-size:9.5px;line-height:15px;font-weight:700}
.post-text{font-size:11.4px;line-height:15.5px;color:#555;text-align:justify}
.share{font-size:10px;color:#222}
.share i{display:inline-block;width:14px;height:13px;border:1px solid #888;background:#ddd;vertical-align:middle;margin-left:1px}
.video{left:6px;top:6px;width:238px;height:163px;background:#000}
.footer{left:0;top:1032px;width:961px;height:138px;background:var(--footer)}
.footer-bottom{left:0;top:1170px;width:961px;height:30px;background:var(--footer-bottom)}
.f-title{font-family:"Open Sans",sans-serif;font-size:15px;color:#fff}
.f-list{font-family:"Open Sans",sans-serif;font-size:8.8px;line-height:16.3px;color:var(--footer-text);list-style:none}
.fsep{width:0;border-left:1px solid #3a3a3a}
.social{width:28px;height:27px;font-family:"Open Sans",sans-serif;font-size:6px;color:#fff;text-align:center;line-height:27px;overflow:hidden}
.f-bottom{font-family:"Open Sans",sans-serif;font-size:8px;color:#aaa;left:112px}
</style>
</head>
<body>
<div class="abs hero-bg"></div>

<header>
  <div class="abs brand">
    <div class="brand-name">Crestline</div>
    <div class="brand-tag">INDOOR ROWING CENTER</div>
  </div>
  <a class="abs btn-login">Login Now »</a>
  <a class="abs btn-register">Register Now</a>
  <div class="abs search">Search Keyword</div>
  <div class="abs search-btn">
    <svg width="31" height="26" viewBox="0 0 31 26"><circle cx="14" cy="12" r="4.5" fill="none" stroke="#fff" stroke-width="2"/><line x1="17.5" y1="15.5" x2="21" y2="19" stroke="#fff" stroke-width="2.4"/></svg>
  </div>
  <nav class="abs nav">
    <div class="abs nav-home">
      <svg width="41" height="36" viewBox="0 0 41 36"><path d="M11 19 L20.5 10 L30 19" fill="none" stroke="#222" stroke-width="2.5"/><path d="M14 18 V26 H18.5 V21 H22.5 V26 H27 V18" fill="#222"/></svg>
    </div>
    <span class="abs nav-item" style="left:57px">Company Info</span>
    <span class="abs nav-sep" style="left:143px"></span>
    <span class="abs nav-item" style="left:169px">Coaches</span>
    <span class="abs nav-sep" style="left:231px"></span>
    <span class="abs nav-item" style="left:259px">Programs</span>
    <span class="abs nav-sep" style="left:325px"></span>
    <span class="abs nav-item" style="left:353px">Blog</span>
    <span class="abs nav-sep" style="left:400px"></span>
    <span class="abs nav-item" style="left:426px">Contact</span>
    <span class="abs nav-sep" style="left:490px"></span>
    <span class="abs nav-item" style="left:512px">Donate</span>
    <span class="abs nav-sep" style="left:569px"></span>
  </nav>
</header>

<section class="abs slider">
  <div class="abs slide" role="img" aria-label="Photo of a woman training on an indoor rowing machine in a gym"></div>
  <div class="abs arrow" style="left:20px;top:143px"><svg width="32" height="32"><path d="M18 10 L12 16 L18 22" fill="none" stroke="#666" stroke-width="1.5"/></svg></div>
  <div class="abs arrow" style="left:763px;top:143px"><svg width="32" height="32"><path d="M14 10 L20 16 L14 22" fill="none" stroke="#666" stroke-width="1.5"/></svg></div>
</section>

<section class="abs welcome">
  <h1>Welcome to Crestline Indoor Rowing Center</h1>
  <div class="abs rule" style="left:29px;top:51px;width:783px"></div>
  <p style="top:57px"><strong>At Crestline we provide group fitness classes for the novice to elite rower.</strong> What makes our fitness classes so unique is the opportunity to workout in a group setting along with having an instructor give individual attention on rowing bio mechanics and training. Our center features a private erg room for 15 Norvex 7 rowing machines along with smaller rooms for live online rowing with your teammates and others from around the world.</p>
  <p style="top:111px">Rather your an experience rower training for the sprint season or a new rower looking for a fun and effective workout we have a variety of classes to choose from to meet your needs. Check out our programs and classes and sign up today.</p>
  <a class="abs btn-dark" style="left:325px;top:156px;width:197px;height:34px;font-size:15px;line-height:26px">Click here for more details »</a>
</section>

<main>
  <h2 class="abs col-title" style="left:84px"><span>Our</span> Programs</h2>
  <div class="abs rule" style="left:74px;top:737px;width:248px"></div>
  <div class="abs frame" style="left:71px;top:754px;width:246px;height:112px">
    <div class="abs" style="left:5px;top:5px;width:236px;height:102px;background:linear-gradient(180deg,#f4f4f4,#dcdcdc)" role="img" aria-label="Photo of a man rowing on an indoor ergometer"></div>
  </div>
  <p class="abs copy" style="left:75px;top:885px;width:241px">Nullam accumsan lorem id quam consequat, nec hendrerit ipsum rhoncus. Nullam at nisl et justo fermentum vehicula eget a velit. Curabitur molestie neque vitae risus semper, mattis vestibulum...</p>
  <a class="abs btn-dark" style="left:133px;top:978px;width:126px;height:29px;font-size:12px;line-height:21px">More Details</a>

  <span class="abs vsep" style="left:341px"></span>

  <h2 class="abs col-title" style="left:359px"><span>Recent</span> Blogs</h2>
  <div class="abs rule" style="left:351px;top:737px;width:257px"></div>

  <article>
    <div class="abs post-title" style="left:357px;top:751px">Vestibulum eget</div>
    <div class="abs post-by" style="left:460px;top:754px;width:152px">[ <b>Posted By :</b> Northgate Media ]</div>
    <div class="abs badge" style="left:356px;top:788px"><div class="top">Dec<b>13th</b></div><div class="bot">2013</div></div>
    <p class="abs post-text" style="left:416px;top:776px;width:194px">Cras non turpis quis ante feugiat ornare. Nulla facilisis vestibulum odio, a male-suada augue sodales non.</p>
    <div class="abs share" style="left:416px;top:830px">Share This <i></i><i></i><i></i><i></i></div>
  </article>
  <article>
    <div class="abs post-title" style="left:357px;top:879px">Vestibulum eget</div>
    <div class="abs post-by" style="left:460px;top:882px;width:152px">[ <b>Posted By :</b> Northgate Media ]</div>
    <div class="abs badge" style="left:356px;top:916px"><div class="top">Dec<b>8th</b></div><div class="bot">2013</div></div>
    <p class="abs post-text" style="left:416px;top:904px;width:194px">Cras non turpis quis ante feugiat ornare. Nulla facilisis vestibulum odio, a male-suada augue sodales non.</p>
    <div class="abs share" style="left:420px;top:958px">Share This <i></i><i></i><i></i><i></i></div>
  </article>

  <span class="abs vsep" style="left:619px"></span>

  <h2 class="abs col-title" style="left:635px"><span>Coaching</span> Analysis</h2>
  <div class="abs rule" style="left:628px;top:737px;width:253px"></div>
  <div class="abs frame" style="left:631px;top:754px;width:249px;height:181px">
    <div class="abs video">
      <div class="abs" style="left:20px;top:3px;font-size:5.5px;color:#ddd;font-family:Arial,sans-serif">Box Selection and Multi-Line Editing Demo</div>
      <div class="abs" style="left:0;top:12px;width:238px;border-top:1px solid #333"></div>
      <svg class="abs" style="left:100px;top:50px" width="38" height="38"><circle cx="19" cy="19" r="16" fill="none" stroke="#fff" stroke-width="2.5"/><path d="M14 10 L28 19 L14 28Z" fill="#fff"/></svg>
      <div class="abs" style="left:0;top:92px;width:238px;text-align:center;font-size:6px;color:#ccc;font-family:Arial,sans-serif">click to play</div>
      <div class="abs" style="left:0;top:141px;width:238px;height:22px;background:#222;border-top:2px solid #555"></div>
      <div class="abs" style="left:6px;top:144px;font-size:5px;line-height:8px;color:#ccc;font-family:Arial,sans-serif">▸ video options<br>▸ playlist (1)</div>
      <svg class="abs" style="left:110px;top:145px" width="16" height="16"><circle cx="8" cy="8" r="6.5" fill="none" stroke="#fff" stroke-width="1.3"/><path d="M6 5 L11 8 L6 11Z" fill="#fff"/></svg>
      <div class="abs" style="left:198px;top:152px;width:22px;border-top:2px solid #ccc"></div>
    </div>
  </div>
  <p class="abs copy" style="left:636px;top:946px;width:242px">Nullam at nisl et justo fermentum vehicula eget a velit. Curabitur molestie neque vitae risus semper, mattis vestibulum libero dapibus.</p>
</main>

<footer>
  <div class="abs footer">
    <h3 class="abs f-title" style="left:138px;top:10px">Quick Links</h3>
    <ul class="abs f-list" style="left:141px;top:35px">
      <li>Lorem ipsum dolor sit</li><li>Amet consectetuer</li><li>Adipiscing elit</li><li>Praesent vestibulum</li><li>Molestie lacus aenean</li>
    </ul>
    <span class="abs fsep" style="left:287px;top:31px;height:97px"></span>
    <h3 class="abs f-title" style="left:331px;top:10px">How it Works</h3>
    <ul class="abs f-list" style="left:334px;top:35px">
      <li>Lorem ipsum dolor sit</li><li>Amet consectetuer</li><li>Adipiscing elit</li><li>Praesent vestibulum</li><li>Molestie lacus aenean</li>
    </ul>
    <span class="abs fsep" style="left:472px;top:31px;height:97px"></span>
    <h3 class="abs f-title" style="left:500px;top:12px">Contact Us</h3>
    <ul class="abs f-list" style="left:502px;top:37px">
      <li>34 Crestline Indoor</li><li>Millbrook, MB4 2QT</li><li>Phone:+44(0)1632 960418</li><li>Email:info@crestlineindoor.example</li>
    </ul>
    <div class="abs social" style="left:693px;top:14px;background:#f26a10">Feed</div>
    <div class="abs social" style="left:724px;top:14px;background:#3b5998">Chatterloop</div>
    <div class="abs social" style="left:756px;top:14px;background:#c5362b">Vantrix+</div>
    <div class="abs social" style="left:793px;top:14px;background:#2aa3df">Chirpline</div>
    <div class="abs" style="left:672px;top:58px;width:150px;border-top:1px solid #3a3a3a"></div>
    <div class="abs" style="left:688px;top:78px;text-align:center">
      <div style="font-family:'Fredoka',sans-serif;font-size:27px;line-height:28px;color:#bbb">Crestline</div>
      <div style="font-family:'Open Sans',sans-serif;font-weight:600;font-size:6px;letter-spacing:1.9px;color:#bbb">INDOOR ROWING CENTER</div>
    </div>
  </div>
  <div class="abs footer-bottom">
    <div class="abs f-bottom" style="top:3px">Home &nbsp;| &nbsp;Info &nbsp;| &nbsp;Coaches &nbsp;| &nbsp;Programs &nbsp;| &nbsp;Blog &nbsp;| &nbsp;Contact &nbsp;| &nbsp;Donate!</div>
    <div class="abs f-bottom" style="top:17px">© 2013 Crestline Indoor Rowing Center. &nbsp;&nbsp;FAQ &nbsp;| &nbsp;Privacy Policy &nbsp;| &nbsp;Site Map.</div>
  </div>
</footer>
</body>
</html>
```